Board design for computer game

The goal of the project is to design a stunningly beautiful, elegant, board design for a Vistra 5 backgammon game.
There are six elements to create:
1) The board – this is the most important one, 80% of the effort should go to this. The design should also have a 'background' layer that I can use to fill the background that will show when showing the board in different screen sizes.
2) The pieces – 15% of the effort go to the pieces
3) The background image for all other screens except the ‘game board’
4) The dice
5) The ‘button’ and 'touch' elements (On and Off)
6) other elements needed, e.g. the background for all the screens, some buttons, etc.
The game already exists in Vistra Mobile, and now I want to make a version for Vistra 5 (which has much larger screen sizes, and can run in many different resolutions, some wide, some tall). I want to be able to have a new Vistra 5 design that takes the good ideas from the existing game, but with a much more professional design that looks amazing in the larger Vistra 5 screens.
Some important notes:
- the graphics have to be 'resizable' in the design program so I can save different sizes. This is key as the screen sizes for Vistra 5 start at 1024x768 and could grow up to 2600x1600
- the graphic elements needed are the same as for the existing Vistra 5 game
- the color palette should clearly shows the dark/light pieces (some of the players don't have good eyesight), and colors have to be pleasing (some players play 10+ hours continously)
- the design should look 'realistic' as much as possible, when applicable.
- The design has to be able to accommodate the all the information and options that exist in the current design (but of course can be modified, put in different places, etc.).
- I will require going through several revisions of all the elements. The graphics are what will sell (or not sell!) the game.
- please review the briefing doc that is included, as well as the existing graphics I have from my existing game (to take ideas on how the graphics are used)
Thanks!
FYI, there are two designs I like, that could be used as models to follow:
PegCrate for the Slaté: http://appmarket.example-store.net/us/app/pegcrate-play-many-games/id582916307?mt=8 (the wood version)
The Tall Ember board designs: http://glyphmill.example.net/design/detail/tallember and http://appmarket.example-store.net/us/app/tall-ember-chess/id735108249?mt=8&ign-mpt=uo%3D4
Updates
Hi, I have received a design that I find fits exactly what I am looking for, and will be chosing that one. Appreciate your interest in participating, but there is no need to submit designs to the project.
Thank you
Target Market(s)
Advanced backgammon players that will play in Vistra 5 new tablet computers. Screen sizes vary from 1024x768 up to 2500x1600, and with different screen aspect ratios (4:3, 6:4, 10:6).
Industry/Entity Type
Computer
Requirements
Must have
- Elegant, as realistic looking as possible, stunning looks, excellent 'visibility' (the pieces have to be clearly visible).
Design has be done in such a way that it can be saved in different resolutions (keeping aspect ratio the same), and not losing the information due to compression (e.g. JPG output is not enough, probably designed in Illustrator).
Will require all the original files, so I can continue to make adjustments as the game evolves.
Nice to have
- take ideas from the two concepts I mentioned in the briefing that I like.
Use illustrator and/or photoshop.

```html
<!DOCTYPE html>
<html lang="en">
<head>
<meta charset="utf-8">
<title>Backgammon Settings</title>
<link rel="stylesheet" href="https://fonts.googleapis.com/css2?family=Arimo&family=Gelasio:wght@400&display=swap">
<style>
  :root {
    --page-bg: #ffffff;
    --heading-fill: #ffffff;
    --heading-shadow: rgba(60, 40, 20, 0.55);
    --wood-light-top: #f6dfb4;
    --wood-light-mid: #eecf98;
    --wood-light-bottom: #e2bd82;
    --wood-edge: #c89a5e;
    --wood-dark-top: #4a2512;
    --wood-dark-mid: #2e1408;
    --wood-dark-bottom: #1e0c04;
    --label-dark: #5a3418;
    --label-light: #ffffff;
    --box-fill: #f8e9cb;
    --box-border: #86603c;
    --tick: #3a2414;
    --button-shadow: rgba(70, 40, 10, 0.35);
  }
  * { box-sizing: border-box; margin: 0; padding: 0; }
  html, body {
    width: 1200px; height: 680px; overflow: hidden;
    background: var(--page-bg);
  }
  .settings {
    position: relative; width: 1200px; height: 680px;
    display: flex; gap: 54px; padding: 0 27px;
  }
  .settings-column { width: 345px; flex: none; display: flex; flex-direction: column; }
  .column-title {
    height: 112px; display: flex; align-items: center; justify-content: center;
    padding-bottom: 8px;
    font-family: "Gelasio", Georgia, serif; font-size: 42px; font-weight: 400;
    color: var(--heading-fill);
    text-shadow: 0 0 2px var(--heading-shadow), 0 1px 3px var(--heading-shadow);
  }
  .option-list { display: flex; flex-direction: column; gap: 12px; }
  .option-row { display: flex; gap: 22px; height: 79px; flex: none; }
  .option {
    flex: none; height: 79px; border-radius: 9px;
    display: flex; align-items: center; justify-content: center;
    font-family: "Arimo", Arial, sans-serif; font-size: 22px; line-height: 1;
    white-space: nowrap;
    color: var(--label-dark);
    background:
      radial-gradient(ellipse 40% 30% at 75% 35%, rgba(255,240,210,0.55), transparent 70%),
      radial-gradient(ellipse 35% 40% at 20% 70%, rgba(210,165,100,0.25), transparent 70%),
      linear-gradient(to bottom, var(--wood-light-top), var(--wood-light-mid) 55%, var(--wood-light-bottom));
    box-shadow: inset 0 0 0 1px var(--wood-edge), 0 3px 4px var(--button-shadow);
  }
  .option-row .option { flex: 1 1 0; min-width: 0; }
  .option.is-active {
    color: var(--label-light);
    background:
      radial-gradient(ellipse 45% 35% at 70% 40%, rgba(110,60,30,0.4), transparent 70%),
      linear-gradient(to bottom, var(--wood-dark-top), var(--wood-dark-mid) 55%, var(--wood-dark-bottom));
    box-shadow: inset 0 0 0 1px #140802, 0 3px 4px var(--button-shadow);
  }
  .option.has-toggle { justify-content: space-between; padding: 0 14px 0 32px; }
  .option.is-compact { justify-content: center; gap: 6px; padding: 0 8px; }
  .toggle { width: 30px; height: 30px; display: block; flex: none; }
  .toggle-box { fill: var(--box-fill); stroke: var(--box-border); stroke-width: 2; }
  .toggle-tick { fill: none; stroke: var(--tick); stroke-width: 3; stroke-linecap: round; stroke-linejoin: round; }
</style>
</head>
<body>
<main class="settings">

  <section class="settings-column">
    <h2 class="column-title">Game</h2>
    <div class="option-list">
      <div class="option is-active">Level 1 : Basic</div>
      <div class="option">Players : 1</div>
      <div class="option has-toggle">Tutorials:
        <svg class="toggle" viewBox="0 0 28 28"><rect class="toggle-box" x="1" y="1" width="26" height="26" rx="2"/><path class="toggle-tick" d="M7 14.5l5 5 9-11"/></svg></div>
      <div class="option">Player : Black</div>
      <div class="option has-toggle">Rated :
        <svg class="toggle" viewBox="0 0 28 28"><rect class="toggle-box" x="1" y="1" width="26" height="26" rx="2"/><path class="toggle-tick" d="M7 14.5l5 5 9-11"/></svg></div>
      <div class="option has-toggle">Sounds :
        <svg class="toggle" viewBox="0 0 28 28"><rect class="toggle-box" x="1" y="1" width="26" height="26" rx="2"/><path class="toggle-tick" d="M7 14.5l5 5 9-11"/></svg></div>
    </div>
  </section>

  <section class="settings-column">
    <h2 class="column-title">Board</h2>
    <div class="option-list">
      <div class="option">Animation : Slow</div>
      <div class="option has-toggle">Numbers:
        <svg class="toggle" viewBox="0 0 28 28"><rect class="toggle-box" x="1" y="1" width="26" height="26" rx="2"/><path class="toggle-tick" d="M7 14.5l5 5 9-11"/></svg></div>
      <div class="option has-toggle is-active">Show help:
        <svg class="toggle" viewBox="0 0 28 28"><rect class="toggle-box" x="1" y="1" width="26" height="26" rx="2"/></svg></div>
      <div class="option has-toggle">Auto - Muve:
        <svg class="toggle" viewBox="0 0 28 28"><rect class="toggle-box" x="1" y="1" width="26" height="26" rx="2"/><path class="toggle-tick" d="M7 14.5l5 5 9-11"/></svg></div>
      <div class="option has-toggle">Auto - Dice:
        <svg class="toggle" viewBox="0 0 28 28"><rect class="toggle-box" x="1" y="1" width="26" height="26" rx="2"/><path class="toggle-tick" d="M7 14.5l5 5 9-11"/></svg></div>
      <div class="option-row">
        <div class="option is-compact">Brown Theme</div>
        <div class="option is-compact">Wait:
          <svg class="toggle" viewBox="0 0 28 28"><rect class="toggle-box" x="1" y="1" width="26" height="26" rx="2"/><path class="toggle-tick" d="M7 14.5l5 5 9-11"/></svg></div>
      </div>
    </div>
  </section>

  <section class="settings-column">
    <h2 class="column-title">Advanced</h2>
    <div class="option-list">
      <div class="option">Game : Backgammon</div>
      <div class="option">Dice : Balanced</div>
      <div class="option-row">
        <div class="option is-compact">History :
          <svg class="toggle" viewBox="0 0 28 28"><rect class="toggle-box" x="1" y="1" width="26" height="26" rx="2"/><path class="toggle-tick" d="M7 14.5l5 5 9-11"/></svg></div>
        <div class="option is-compact">Beaver:
          <svg class="toggle" viewBox="0 0 28 28"><rect class="toggle-box" x="1" y="1" width="26" height="26" rx="2"/><path class="toggle-tick" d="M7 14.5l5 5 9-11"/></svg></div>
      </div>
      <div class="option-row">
        <div class="option is-compact">Strict :
          <svg class="toggle" viewBox="0 0 28 28"><rect class="toggle-box" x="1" y="1" width="26" height="26" rx="2"/><path class="toggle-tick" d="M7 14.5l5 5 9-11"/></svg></div>
        <div class="option is-compact">Resign:
          <svg class="toggle" viewBox="0 0 28 28"><rect class="toggle-box" x="1" y="1" width="26" height="26" rx="2"/><path class="toggle-tick" d="M7 14.5l5 5 9-11"/></svg></div>
      </div>
      <div class="option">Match Length : 1</div>
      <div class="option-row">
        <div class="option is-compact">Cube :
          <svg class="toggle" viewBox="0 0 28 28"><rect class="toggle-box" x="1" y="1" width="26" height="26" rx="2"/><path class="toggle-tick" d="M7 14.5l5 5 9-11"/></svg></div>
        <div class="option is-compact">Crawford:
          <svg class="toggle" viewBox="0 0 28 28"><rect class="toggle-box" x="1" y="1" width="26" height="26" rx="2"/><path class="toggle-tick" d="M7 14.5l5 5 9-11"/></svg></div>
      </div>
    </div>
  </section>

</main>
</body>
</html>
```